Corvane Partners Web Design

Dear all
I need a web design for a financial services site. We are a broker who deals with many different financial institutions and require a clean, simple and instantly impressive site based on the colour scheme that SketchGuild created for us. A landing page (www.crvnp.mx) gives an idea of the logo and clour scheme but we are looking at either a one page site with rollover text boxes or a 3 or 4 page site depending on the preference of the designer and the best user experience. The site“s purpose is to give confidence that the company exists rather than impart pages of information although we would like this to be a site that can expand over time as the company grows. For now the requirement is for a clear set of possibly changing images at the centre of a white screen that relate to finance in general nad the benefits of wealth creation as well as sectios either along the top or bottom - Our Company, Our Approach, Our services, Our clients, Contact (user to fill in contact box to be sent to info@crvnp.mx. The text for each of these boxes I assume can be added by the coding team here, it the overall look and feel that I am looking for from SketchGuild - deadline can be extended if necessary but I was hoping to wrap this all up in October

Target Market(s)

Succesful individuals looking to maximise returns on their investment via world class financial institutions and supported throughout by qualified independent financial advisors

Industry/Entity Type

Finance

Requirements
Must have
• Logo and color scheme of the logo design SketchGuild sent - I have all these sourcefiles, pantone and fonts

```html
<!DOCTYPE html>
<html lang="en">
<head>
<meta charset="utf-8">
<title>Corvane Partners – Wealth Management</title>
<link rel="stylesheet" href="https://fonts.googleapis.com/css2?family=Comfortaa:wght@400;600&family=Arimo:wght@400;700&family=Roboto:wght@300;400&display=swap">
<style>
:root{
  --navy:#1c3a63;
  --orange:#eea136;
  --grey-band:#f0f0f0;
  --footer-nav:#878d91;
  --footer-bg:#f2f2f2;
  --text:#444;
  --steel:#8b8e93;
  --white:#fff;
}
*{box-sizing:border-box;margin:0;padding:0}
html,body{width:1200px;height:1060px;overflow:hidden;background:var(--white);font-family:"Arimo",Arial,sans-serif}
.page{position:relative;width:1200px;height:1060px}
.brand{position:absolute;left:0;top:14px;width:1200px;text-align:center}
.brand-mark{display:block;margin:0 auto;width:74px;height:74px;border-radius:50%;background:var(--navy)}
.brand-name{margin-top:22px;font-family:"Comfortaa",sans-serif;font-weight:400;font-size:26px;letter-spacing:14px;color:var(--navy);padding-left:14px}
.brand-tagline{margin-top:26px;font-family:"Comfortaa",sans-serif;font-size:17px;letter-spacing:2px;color:var(--navy)}
.nav-rule{position:absolute;left:210px;top:207px;width:780px;height:1px;background:linear-gradient(90deg,transparent,#ddd 20%,#ddd 80%,transparent)}
.main-nav{position:absolute;left:248px;top:219px;display:flex;gap:13px}
.main-nav a{display:block;width:106px;height:29px;line-height:29px;text-align:center;font-size:12px;color:var(--white);text-decoration:none;background:var(--navy);border-radius:2px}
.main-nav a.is-active{background:var(--orange)}
.hero{position:absolute;left:0;top:260px;width:1200px;height:328px;background:var(--grey-band)}
.slide-frame{position:absolute;left:350px;top:24px;width:500px;height:268px;background:#d5dde6;padding:5px}
.slide-shadow{position:absolute;left:370px;top:288px;width:460px;height:14px;border-radius:50%;background:radial-gradient(ellipse at center,rgba(0,0,0,.45),transparent 70%)}
.slide-photo{width:490px;height:258px;background:linear-gradient(100deg,#9cc25a 0%,#c79773 35%,#7aa942 60%,#6f9a3a 100%)}
.slide-caption{position:absolute;left:102px;top:191px;width:296px;height:30px;background:var(--white);font-family:"Roboto",sans-serif;font-weight:300;font-size:21px;line-height:30px;text-align:center;color:var(--steel)}
.slide-caption strong{font-weight:400;color:var(--navy)}
.slider-arrow{position:absolute;top:124px;width:68px;height:68px}
.slider-arrow.prev{left:160px}.slider-arrow.next{left:971px}
.features{position:absolute;left:0;top:614px;width:1200px}
.feature{position:absolute;top:0;width:188px;text-align:center}
.feature-icon{display:block;margin:0 auto;width:84px;height:84px;border-radius:50%;background:var(--navy);position:relative;z-index:1;border:2px solid var(--white)}
.feature-title{margin-top:-8px;height:43px;border:1px solid #cfcfcf;border-radius:2px;background:linear-gradient(#fff,#f1f1f1);font-family:"Comfortaa",sans-serif;font-size:19px;line-height:46px;color:var(--navy);letter-spacing:1px}
.feature-text{margin-top:18px;font-size:11.4px;line-height:14px;color:var(--text)}
.read-more{display:block;margin:17px auto 0;width:88px;height:26px;line-height:26px;background:var(--orange);color:var(--white);font-size:12px;text-decoration:none;border-radius:2px}
.footer-nav{position:absolute;left:0;top:878px;width:1200px;height:28px;background:var(--footer-nav);display:flex;justify-content:center;align-items:center;font-size:11.5px;color:var(--white)}
.footer-nav a{color:var(--white);text-decoration:none}
.footer-nav .sep{margin:0 17px;opacity:.8}
.contact{position:absolute;left:0;top:906px;width:1200px;height:154px;background:var(--footer-bg);text-align:center}
.contact h2{margin-top:20px;font-size:18px;font-weight:700;color:var(--navy)}
.contact-rule{width:350px;height:1px;margin:8px auto 0;background:linear-gradient(90deg,transparent,#ddd,transparent)}
.contact-line{margin-top:12px;font-size:11.5px;color:var(--navy)}
.contact-line b{font-weight:700}
.contact-line .sep{margin:0 14px;color:#666}
.social{display:flex;justify-content:center;gap:10px;margin-top:12px}
.social span{width:20px;height:20px;background:#3a6fa8;border-radius:2px}
.copyright{margin-top:14px;font-size:10.5px;color:#777}
.copyright b{color:#666}
</style>
</head>
<body>
<div class="page">
  <header class="brand">
    <span class="brand-mark" aria-hidden="true"></span>
    <div class="brand-name">CORVANE PARTNERS</div>
    <div class="brand-tagline">WEALTH MANAGEMENT</div>
  </header>
  <div class="nav-rule"></div>
  <nav class="main-nav">
    <a href="#" class="is-active">Home</a>
    <a href="#">Our Company</a>
    <a href="#">Our Approach</a>
    <a href="#">Our services</a>
    <a href="#">Our clients</a>
    <a href="#">Contact us</a>
  </nav>

  <section class="hero">
    <svg class="slider-arrow prev" viewBox="0 0 68 68" aria-label="Previous slide"><circle cx="34" cy="34" r="32.5" fill="none" stroke="#8b8e93" stroke-width="2"/><polyline points="40,18 25,34 40,50" fill="none" stroke="#8b8e93" stroke-width="2.5"/></svg>
    <div class="slide-shadow"></div>
    <div class="slide-frame">
      <div class="slide-photo" role="img" aria-label="Photo of hands holding soil with a young green plant"></div>
      <div class="slide-caption">Secure Your <strong>Education</strong> With Us</div>
    </div>
    <svg class="slider-arrow next" viewBox="0 0 68 68" aria-label="Next slide"><circle cx="34" cy="34" r="32.5" fill="none" stroke="#8b8e93" stroke-width="2"/><polyline points="28,18 43,34 28,50" fill="none" stroke="#8b8e93" stroke-width="2.5"/></svg>
  </section>

  <section class="features">
    <article class="feature" style="left:169px">
      <span class="feature-icon" role="img" aria-label="Icon of a rising bar chart with arrow"></span>
      <h3 class="feature-title">Our Company</h3>
      <p class="feature-text">Lorem ipsum dolor sit amet,<br>consectetur adipisicing elit, sed<br>do eiusmod tempor incididunt<br>ut labore et dolore....</p>
      <a class="read-more" href="#">Read More</a>
    </article>
    <article class="feature" style="left:393px">
      <span class="feature-icon" role="img" aria-label="Icon of a person working at a desk"></span>
      <h3 class="feature-title">Our Approach</h3>
      <p class="feature-text">Lorem ipsum dolor sit amet,<br>consectetur adipisicing elit, sed<br>do eiusmod tempor incididunt<br>ut labore et dolore....</p>
      <a class="read-more" href="#">Read More</a>
    </article>
    <article class="feature" style="left:618px">
      <span class="feature-icon" role="img" aria-label="Icon of a person running on gears"></span>
      <h3 class="feature-title">Our Services</h3>
      <p class="feature-text">Lorem ipsum dolor sit amet,<br>consectetur adipisicing elit, sed<br>do eiusmod tempor incididunt<br>ut labore et dolore....</p>
      <a class="read-more" href="#">Read More</a>
    </article>
    <article class="feature" style="left:842px">
      <span class="feature-icon" role="img" aria-label="Icon of two people shaking hands"></span>
      <h3 class="feature-title">Our Clients</h3>
      <p class="feature-text">Lorem ipsum dolor sit amet,<br>consectetur adipisicing elit, sed<br>do eiusmod tempor incididunt<br>ut labore et dolore....</p>
      <a class="read-more" href="#">Read More</a>
    </article>
  </section>

  <nav class="footer-nav">
    <a href="#">Home</a><span class="sep">|</span>
    <a href="#">Our Company</a><span class="sep">|</span>
    <a href="#">Our Approach</a><span class="sep">|</span>
    <a href="#">Our services</a><span class="sep">|</span>
    <a href="#">Our clients</a><span class="sep">|</span>
    <a href="#">Contact us</a>
  </nav>

  <footer class="contact">
    <h2>Get In Touch</h2>
    <div class="contact-rule"></div>
    <p class="contact-line"><b>Tel :</b> +52 (55) 4817 2093<span class="sep">|</span><b>Email :</b> info@crvnp.mx</p>
    <div class="social"><span aria-label="Social link 1"></span><span aria-label="Social link 2"></span><span aria-label="Social link 3"></span></div>
    <div class="contact-rule" style="margin-top:12px"></div>
    <p class="copyright">Copyright © <b>Corvane Partners</b> 2013.All Right Reserved.</p>
  </footer>
</div>
</body>
</html>
```